I need 2 flyers designed for my business

Both can be similar in design and will have different purposes. I need an education based flyer and I need a government based flyer. The focus of the flyer will be software on the front and services on the back.
These all need to be 8.5x 11 in dimension (they can be full bleed). I would like to be able to print these out if needed. The design needs to look good with our website > www.brintalo.com

The software details are on the website.

```html
<!DOCTYPE html>
<html lang="en">
<head>
<meta charset="utf-8">
<title>Brintalo Records Flyers</title>
<link rel="stylesheet" href="https://fonts.googleapis.com/css2?family=Montserrat:ital,wght@0,600;0,700;0,800;1,800&family=Roboto:wght@400;700;900&display=swap">
<style>
  :root {
    --maroon: #861a1d;
    --maroon-deep: #6e1215;
    --white: #ffffff;
    --stage: #e6e6e6;
    --blue: #1c6fc4;
    --blue-deep: #1d4ba8;
    --blue-light: #3d8fe0;
  }
  * { margin: 0; padding: 0; box-sizing: border-box; }
  html, body { width: 713px; height: 1200px; overflow: hidden; }
  body { background: var(--stage); position: relative; font-family: "Roboto", sans-serif; }

  .flyer { position: absolute; left: 136px; width: 440px; height: 569px; overflow: hidden; }
  .flyer-front { top: 20px; background: var(--maroon); }
  .flyer-back { top: 611px; background: linear-gradient(160deg, var(--blue-deep) 0%, var(--blue) 55%, #1a78c9 100%); }
  .flyer svg.shapes { position: absolute; inset: 0; }

  .brand-name { position: absolute; font-family: "Montserrat", sans-serif; font-weight: 700; color: var(--maroon); line-height: 1; }
  .front-brand { left: 258px; top: 38px; font-size: 19px; }
  .front-brand .dot, .back-brand .dot { display: inline-block; width: 12px; height: 12px; border-radius: 50%; background: var(--maroon); margin-right: 7px; vertical-align: -1px; }

  .front-title { position: absolute; left: 0; right: 0; top: 160px; text-align: center; font-family: "Montserrat", sans-serif; font-weight: 800; font-style: italic; color: var(--white); font-size: 28px; line-height: 43px; }

  .feature { position: absolute; background: var(--white); border-radius: 24px; box-shadow: 3px 3px 7px rgba(0,0,0,0.18); font-family: "Montserrat", sans-serif; font-weight: 700; color: var(--maroon); font-size: 10.5px; line-height: 12.5px; display: flex; align-items: center; padding-left: 20px; height: 46px; }
  .product-badge { position: absolute; left: 156px; top: 363px; width: 114px; height: 114px; border-radius: 50%; border: 2.5px solid var(--maroon); background: var(--white); display: flex; align-items: center; justify-content: center; font-family: "Montserrat", sans-serif; font-weight: 700; color: var(--maroon); font-size: 24px; }

  .circuit-art { position: absolute; left: 250px; top: 150px; width: 190px; height: 330px; background: radial-gradient(ellipse at 80% 60%, rgba(120,200,255,0.55), rgba(40,110,210,0) 70%); }
  .back-brand-box { position: absolute; left: 252px; top: 33px; width: 152px; height: 52px; background: var(--white); display: flex; align-items: center; padding-left: 12px; }
  .back-brand { position: static; font-size: 15px; }

  .services-title { position: absolute; left: 36px; top: 110px; font-family: "Roboto", sans-serif; font-weight: 900; font-size: 48px; color: var(--white); letter-spacing: -0.5px; }
  .intro { position: absolute; left: 36px; top: 175px; width: 370px; font-size: 7.5px; line-height: 10px; color: var(--white); }
  .service { position: absolute; left: 36px; width: 300px; color: var(--white); }
  .service h2 { display: flex; align-items: center; gap: 12px; font-weight: 700; font-size: 15.5px; }
  .service h2 svg { width: 22px; height: 22px; flex: none; }
  .service p { font-size: 7.5px; line-height: 10px; margin-top: 12px; }
  .contact { position: absolute; right: 20px; top: 530px; text-align: right; color: var(--white); font-size: 7.5px; line-height: 10px; }
</style>
</head>
<body>

<section class="flyer flyer-front">
  <svg class="shapes" viewBox="0 0 440 569" aria-hidden="true">
    <path d="M100 0 H440 V124 H210 C150 124 105 80 100 0 Z" fill="#ffffff"/>
    <path d="M0 554 V380 C0 320 40 288 100 288 H440 V540 C440 548 432 554 424 554 Z" fill="#ffffff"/>
    <rect x="0" y="554" width="440" height="15" fill="#6e1215"/>
  </svg>
  <div class="brand-name front-brand"><span class="dot"></span>Brintalo<br><span style="padding-left:19px">Records</span></div>
  <h1 class="front-title">Record Management<br>Services &amp; Software</h1>

  <div class="feature" style="left:57px;top:320px;width:98px">Document<br>Archive</div>
  <div class="feature" style="left:283px;top:320px;width:97px">HR<br>Onboarding</div>
  <div class="feature" style="left:26px;top:398px;width:98px">Electronic<br>Forms &amp;<br>Workflows</div>
  <div class="feature" style="left:318px;top:398px;width:93px">eSigning</div>
  <div class="feature" style="left:57px;top:474px;width:98px">Mileage &amp;<br>Expense<br>Tracking</div>
  <div class="feature" style="left:280px;top:474px;width:100px">Scanning &amp;<br>Database<br>Conversion</div>
  <div class="product-badge">Archly</div>
</section>

<section class="flyer flyer-back">
  <div class="circuit-art" role="img" aria-label="Glowing blue circuit board traces"></div>
  <div class="back-brand-box"><div class="brand-name back-brand"><span class="dot"></span>Brintalo Records</div></div>
  <h1 class="services-title">Services</h1>
  <p class="intro">Brintalo Records offers comprehensive records management services, including secure, offsite document storage, online document hosting, document conversion services, and enterprise solutions, for businesses of all sizes.</p>

  <div class="service" style="top:238px">
    <h2><svg viewBox="0 0 24 24" fill="none" stroke="#fff" stroke-width="2"><circle cx="12" cy="12" r="4"/><path d="M12 2v4M12 18v4M2 12h4M18 12h4M5 5l3 3M16 16l3 3M5 19l3-3M16 8l3-3"/></svg>Software</h2>
    <p>Access all of your records – whether active or inactive – through Archly, our comprehensive records management software.</p>
  </div>
  <div class="service" style="top:308px">
    <h2><svg viewBox="0 0 24 24" fill="none" stroke="#fff" stroke-width="1.8"><path d="M2 9l10-5 10 5-10 5z"/><path d="M2 13l10 5 10-5M2 17l10 5 10-5"/></svg>Scanning</h2>
    <p>Rediscover your office space by letting us store your records offsite.</p>
  </div>
  <div class="service" style="top:381px">
    <h2><svg viewBox="0 0 24 24" fill="#fff"><rect x="2" y="3" width="20" height="5"/><rect x="3" y="10" width="18" height="11"/><rect x="9" y="12" width="6" height="2" fill="#1c6fc4"/></svg>Storage</h2>
    <p>Rediscover your office space by letting us store your records offsite.</p>
  </div>
  <div class="service" style="top:457px">
    <h2><svg viewBox="0 0 24 24" fill="none" stroke="#fff" stroke-width="1.8"><path d="M7 2h7l4 4v7H7z"/><rect x="4" y="13" width="16" height="4"/><path d="M7 17v5M10 17v5M13 17v5M16 17v5"/></svg>Shredding</h2>
    <p>Let us destroy paper-based documents you no longer need in a safe,<br>secure, cost-effective manner.</p>
  </div>

  <p class="contact">Phone: (555) 014-2290 | Fax: (555) 014-2291<br>410 Commerce Drive Fairhaven, Ohio 44001</p>
</section>

</body>
</html>
```